Wordpress and Elementor Pro website

We need a Wordpress/Elementor Pro design for our website. We already have a logo design and installed Wordpress. We have some ideas concerning the design, and we will share two websites. Both the design and content placement we like about these websites. We would like to see designs that use the color Purple (the same as the logo color), white and black. We provide these services: SEO optimization, SEO copywriting and online campaigns. We will provide a list of the page's we would like to see in the design.

Target Market(s)

Entrepreneurs, business owners. Companies who would like to expand online with texts and SEO.

Industry/Entity Type

Digital Marketing

Coding

Coded - Design and coding required

Number of Pages Required

5+ page

Font styles to use
Sans Serif

Colors
886aae
fffefd
0355a3

Requirements
Must have
• Single pages and singel posts of Elementor so I can create new pages and blog posts in the future.

```html
<!DOCTYPE html>
<html lang="en">
<head>
<meta charset="utf-8">
<title>Veldhoven Online</title>
<link href="https://fonts.googleapis.com/css2?family=Poppins:wght@400;500;600;700;800;900&display=swap" rel="stylesheet">
<style>
:root{
  --purple:#7a1fe0;
  --purple-deep:#4a1466;
  --purple-logo:#6a3fa0;
  --white:#ffffff;
  --yellow:#ffbf1a;
  --navy:#1f2d3d;
  --navy-btn:#2a3d55;
  --footer:#00203a;
  --blue:#1a9be3;
  --grey-band:#e8e4e3;
  --outline:#d9d9d9;
  --text:#1c1c1c;
}
*{box-sizing:border-box;margin:0;padding:0}
html,body{width:1200px;height:3000px;overflow:hidden;background:var(--white)}
body{position:relative;font-family:'Poppins',sans-serif;color:var(--text)}
.abs{position:absolute}

/* header */
.site-header{left:0;top:0;width:1200px;height:102px;background:var(--white)}
.brand{left:96px;top:30px;display:flex;align-items:center;gap:10px}
.brand-mark{width:26px;height:26px;border:2px solid var(--purple-logo);border-radius:4px}
.brand-name{font-size:22px;font-weight:500;color:var(--purple-logo);letter-spacing:1px}
.nav a{position:absolute;top:40px;font-size:15px;color:#6a3fa0;text-decoration:none;font-weight:400}
.nav .active{font-weight:600;color:var(--purple-deep);border-bottom:2px solid var(--purple-deep);padding-bottom:2px}
.nav .contact-btn{top:30px;height:40px;width:90px;border:2px solid var(--purple-deep);border-radius:8px;display:flex;align-items:center;justify-content:center}
.nav .lang{font-size:13px;font-weight:500;top:42px}

/* hero */
.hero{left:0;top:102px;width:1200px;height:501px;background:linear-gradient(90deg,#7e22e8 0%,#8a2be8 45%,#7c24e2 100%);overflow:hidden}
.hero-scene{left:300px;top:0;width:420px;height:501px;background:linear-gradient(180deg,#6d1fcf,#5a18b3);opacity:.55}
.hero-person{left:122px;top:-62px;width:345px;height:563px;background:linear-gradient(180deg,#e9e1f3,#bfb2cf);border-radius:160px 160px 0 0}
.hero-title{left:751px;top:78px;font-size:43px;line-height:44px;font-weight:900;color:var(--white);text-transform:uppercase}
.hero-title .hl{color:var(--yellow)}
.hero-btn{left:754px;top:374px;width:190px;height:48px;border:2px solid var(--white);border-radius:6px;color:var(--white);font-size:16px;font-weight:500;display:flex;align-items:center;justify-content:center;letter-spacing:.5px}
.hero-arrow{top:206px}

/* section titles */
.title-ghost{font-size:68px;font-weight:600;color:transparent;-webkit-text-stroke:1.5px var(--outline);letter-spacing:3px;text-transform:uppercase;line-height:1}
.title-main{font-size:42px;font-weight:800;color:var(--purple-deep);letter-spacing:2px;text-transform:uppercase;line-height:1}

/* services */
.service-card{top:813px;width:296px;height:381px;background:var(--white);box-shadow:0 2px 10px rgba(0,0,0,.12)}
.service-card svg{position:absolute;left:56px;top:62px}
.service-card h3{position:absolute;left:56px;top:158px;font-size:13px;font-weight:600;letter-spacing:.5px;color:#222}
.service-card p{position:absolute;left:56px;top:186px;width:200px;font-size:14px;line-height:18px;color:#333}
.read-more{position:absolute;left:56px;top:282px;width:115px;height:33px;border-radius:17px;background:var(--navy-btn);color:var(--white);font-size:10px;font-weight:600;display:flex;align-items:center;justify-content:center;letter-spacing:.5px}

/* about */
.about-band{left:0;top:1468px;width:1200px;height:518px;background:var(--navy)}
.about-photo{left:33px;top:1287px;width:637px;height:699px;background:linear-gradient(180deg,#3a4657,#26313f);border-radius:200px 200px 0 0}
.about-lead{left:688px;top:1602px;width:420px;font-size:15px;line-height:21px;font-weight:600;color:var(--white)}
.about-body{left:688px;top:1665px;width:420px;font-size:14.5px;line-height:21px;color:var(--white)}

/* partners */
.partners{left:0;top:1986px;width:1200px;height:158px;background:var(--grey-band)}
.partner{top:2026px;width:72px;height:72px;border-radius:50%;background:#e2671f;opacity:.85}

/* contact */
.touch-text{left:96px;top:2393px;width:400px;font-size:14.5px;line-height:21px;color:#222}
.quick-title{left:743px;top:2309px;font-size:37px;font-weight:800;color:var(--white)}
.field{left:743px;width:289px;border:2px solid var(--navy-btn);background:var(--white);font-size:12px;color:#333;padding:10px 14px}
.submit{left:743px;top:2627px;width:289px;height:42px;background:#0a2238;color:var(--white);font-size:13px;font-weight:700;letter-spacing:1px;display:flex;align-items:center;justify-content:center}

/* footer */
.footer{left:0;top:2551px;width:1200px;height:449px;background:var(--footer)}
.foot-col h4{font-size:13px;font-weight:600;color:var(--white);margin-bottom:14px}
.foot-col a{display:block;font-size:13px;color:var(--white);text-decoration:none;line-height:30px;margin-left:2px}
.socials{display:flex;gap:7px}
.socials span{width:31px;height:31px;border-radius:50%;background:var(--white)}
.foot-rule{left:94px;top:2893px;width:1012px;height:2px;background:#0d4f82}
.copyright{left:0;top:2928px;width:1200px;text-align:center;font-size:13px;color:var(--white)}
.copyright span{color:var(--blue)}
</style>
</head>
<body>

<!-- header -->
<header class="abs site-header">
  <div class="abs brand"><span class="brand-mark"></span><span class="brand-name">VELDHOVEN</span></div>
  <nav class="nav">
    <a class="active" style="left:454px">Home</a>
    <a style="left:537px">Services</a>
    <a style="left:640px">Cases</a>
    <a style="left:727px">Team</a>
    <a style="left:812px">Blog</a>
    <a class="contact-btn" style="left:869px">Contact</a>
    <a class="lang" style="left:984px">Language <span style="color:#aaa">&nbsp;|&nbsp;</span> ▾</a>
  </nav>
</header>

<!-- hero -->
<section class="abs hero">
  <div class="abs hero-scene" role="img" aria-label="Office scene with a thoughtful man at a growth chart"></div>
  <div class="abs hero-person" role="img" aria-label="Cheering woman holding a laptop"></div>
  <h1 class="abs hero-title">Standard<br><span class="hl">dummy text<br>ever since the</span><br>when an<br>unknown<br>printe</h1>
  <div class="abs hero-btn">Get In touch</div>
  <svg class="abs hero-arrow" style="left:32px" width="36" height="76"><polyline points="34,2 2,38 34,74" fill="none" stroke="#fff" stroke-width="1.5"/></svg>
  <svg class="abs hero-arrow" style="left:1128px" width="36" height="76"><polyline points="2,2 34,38 2,74" fill="none" stroke="#fff" stroke-width="1.5"/></svg>
</section>

<!-- services -->
<div class="abs title-ghost" style="left:94px;top:672px">Our Services</div>
<h2 class="abs title-main" style="left:192px;top:708px">Our Services</h2>

<article class="abs service-card" style="left:93px">
  <svg width="60" height="60" viewBox="0 0 60 60" fill="none" stroke="#6a2fb0" stroke-width="2.5"><rect x="4" y="6" width="52" height="38" rx="3"/><line x1="4" y1="14" x2="56" y2="14"/><circle cx="24" cy="29" r="8"/><rect x="44" y="22" width="8" height="20"/><line x1="22" y1="44" x2="22" y2="54"/><line x1="14" y1="54" x2="34" y2="54"/></svg>
  <h3>SEO Copywriting</h3>
  <p>Lorem Ipsum is simply dummy text of the printing and</p>
  <div class="read-more">READ MORE</div>
</article>
<article class="abs service-card" style="left:459px">
  <svg width="64" height="64" viewBox="0 0 64 64" fill="none" stroke="#6a2fb0" stroke-width="2.5"><circle cx="26" cy="26" r="22"/><circle cx="26" cy="26" r="7"/><circle cx="26" cy="26" r="13" stroke-dasharray="5 4"/><line x1="42" y1="42" x2="60" y2="60" stroke-width="5"/></svg>
  <h3>Search Engine Optimization</h3>
  <p>Lorem Ipsum is simply dummy text of the printing and</p>
  <div class="read-more">READ MORE</div>
</article>
<article class="abs service-card" style="left:806px">
  <svg width="62" height="62" viewBox="0 0 62 62" fill="none" stroke="#6a2fb0" stroke-width="2.5"><rect x="6" y="14" width="50" height="36" rx="2"/><rect x="2" y="50" width="58" height="6" fill="#6a2fb0"/><polygon points="22,26 36,18 36,40 22,32" fill="#6a2fb0"/><line x1="14" y1="40" x2="48" y2="40"/><line x1="14" y1="44" x2="40" y2="44"/></svg>
  <h3 style="top:161px">Online Campaigns</h3>
  <p style="top:189px">Lorem Ipsum is simply dummy text of the printing and</p>
  <div class="read-more" style="top:285px">READ MORE</div>
</article>

<!-- about -->
<div class="abs title-ghost" style="left:678px;top:1342px">About Us</div>
<h2 class="abs title-main" style="left:775px;top:1379px">About Us</h2>
<section class="abs about-band"></section>
<div class="abs about-photo" role="img" aria-label="Businessman holding a digital marketing clipboard"></div>
<p class="abs about-lead">Lorem Ipsum is simply dummy text of the printing and typesetting industry.</p>
<p class="abs about-body">Lorem Ipsum has been the industry's standard dummy text ever since the 1500s, when an unknown printer took a galley of type and scrambled it to make a type specimen book. It has survived not only five centuries, but also the leap into electronic typesetting, remaining essentially unchanged. It was popularised in</p>

<!-- partners -->
<section class="abs partners"></section>
<svg class="abs" style="left:94px;top:2048px" width="16" height="36"><polyline points="14,2 2,18 14,34" fill="none" stroke="#999" stroke-width="1.5"/></svg>
<div class="abs partner" style="left:183px"></div>
<div class="abs partner" style="left:340px;border-radius:8px"></div>
<div class="abs partner" style="left:501px;background:#3a2e2e"></div>
<div class="abs partner" style="left:656px;border-radius:8px;background:#8a3a1f"></div>
<div class="abs partner" style="left:803px"></div>
<div class="abs partner" style="left:948px;border-radius:8px;background:#3a2e2e"></div>
<svg class="abs" style="left:1090px;top:2048px" width="16" height="36"><polyline points="2,2 14,18 2,34" fill="none" stroke="#999" stroke-width="1.5"/></svg>

<!-- get in touch -->
<div class="abs title-ghost" style="left:90px;top:2276px">Get In Touch</div>
<h2 class="abs title-main" style="left:229px;top:2316px;color:#000">Get In Touch</h2>
<p class="abs touch-text">Lorem Ipsum is simply dummy text of the printing and typesetting industry.</p>

<!-- footer -->
<footer class="abs footer">
  <div class="abs foot-col" style="left:96px;top:95px"><h4>Sitemap</h4><a>Services</a><a>Cases</a><a>Team</a><a>Blog</a><a>Contact</a></div>
  <div class="abs foot-col" style="left:290px;top:95px"><h4>Information</h4><a>Cookie Policy</a><a>Disclaimer</a><a>Privacy Policy</a></div>
  <div class="abs foot-col" style="left:468px;top:95px"><h4>Follow us on</h4><div class="socials"><span></span><span></span><span></span><span></span><span></span></div></div>
</footer>
<div class="abs foot-rule"></div>
<p class="abs copyright">Copyright © 2020 <span>Veldhoven Online</span></p>

<!-- quick contact -->
<svg class="abs" style="left:0;top:0" width="1200" height="3000" pointer-events="none">
  <polygon points="888,2219 1064,2283 1064,2709 888,2779 712,2709 712,2283" fill="#1a9be3"/>
</svg>
<h3 class="abs quick-title">Quick contact</h3>
<div class="abs field" style="top:2369px;height:41px">Name :</div>
<div class="abs field" style="top:2421px;height:41px">Email:</div>
<div class="abs field" style="top:2472px;height:41px">Phone:</div>
<div class="abs field" style="top:2523px;height:93px">Comments:</div>
<div class="abs submit">SUBMIT NOW</div>

</body>
</html>
```